Oil & Gas Service Brochure

We need to create a brochure that highlights the benefits of one of our services to oil and gas wells. We have a word document that includes a summary of the service and its problem solving benefits as well as some photos. The task will be to create a brochure using this information and our company logo and color schemes. Additionally, copy editing and proofing is preferred.

Target Market(s)

Oil & Gas Well Operators

```html
<!DOCTYPE html>
<html lang="en">
<head>
<meta charset="utf-8">
<title>Wire Burst System – Service Brochure</title>
<link rel="stylesheet" href="https://fonts.googleapis.com/css2?family=Raleway:wght@300;400;600&family=Syncopate:wght@400;700&family=Roboto+Slab:wght@700&family=Tinos:wght@400;700&display=swap">
<style>
  :root{
    --brand-blue:#0c3b8f;
    --brand-navy:#0a2f73;
    --band-grey:#a8aaad;
    --ink:#1b1b1b;
    --paper:#ffffff;
    --backdrop:#5b5c58;
    --grid:#e3e3e3;
    --line:#d2d2d2;
  }
  *{box-sizing:border-box;margin:0;padding:0}
  html,body{width:1200px;height:1200px;overflow:hidden}
  body{background:var(--backdrop);font-family:"Raleway",sans-serif;position:relative}
  .page{position:absolute;top:238px;width:560px;height:724px;background:var(--paper);overflow:hidden}
  .page--front{left:27px}
  .page--back{left:613px}

  .caps{font-family:"Syncopate",sans-serif;font-weight:700;font-variant-caps:small-caps}

  /* front header */
  .front-header{position:absolute;left:0;top:0;width:560px;height:172px}
  .brand{position:absolute;display:flex;align-items:center;gap:12px}
  .brand__mark{width:44px;height:44px;border-radius:50%;background:var(--brand-navy);flex:none}
  .brand__name{font-family:"Syncopate",sans-serif;font-weight:700;font-variant-caps:small-caps;color:var(--brand-blue);line-height:1.05;letter-spacing:1px}
  .brand--header{left:58px;top:21px}
  .brand--header .brand__name{font-size:17px}
  .service-title{position:absolute;left:21px;top:89px;font-size:15.5px;line-height:18.4px;color:var(--paper);letter-spacing:1.2px}
  .service-title .dark{color:var(--ink)}
  .service-title .blue{color:var(--brand-blue)}

  /* blue panels */
  .panel{position:absolute;left:0;width:560px;background:var(--brand-blue);color:var(--paper)}
  .overview{top:172px;height:311px;padding:13px 35px 0 35px}
  .summary{top:199px;height:479px;padding:4px 22px 0 24px}
  .panel h2{font-size:11px;letter-spacing:1.5px;line-height:13px}
  .panel p{font-weight:300;font-size:11px;line-height:12.9px}
  .panel p.lead{text-indent:56px}
  .bullets{list-style:none;margin-top:6px}
  .bullets li{position:relative;padding-left:8px;font-weight:300;font-size:11px;line-height:12.9px;margin-bottom:4px}
  .bullets li::before{content:"›";position:absolute;left:0;top:-1px;font-weight:600}
  .summary .bullets li{margin-bottom:5px;padding-left:9px}

  /* charts */
  .chart{position:absolute;left:0}
  .chart--trend{top:483px;width:560px;height:241px}
  .chart--compare{top:0;width:560px;height:199px}
  .chart text{font-family:"Tinos",serif}
  .chart .chart-title{font-family:"Syncopate",sans-serif;font-weight:700;font-variant-caps:small-caps;fill:var(--brand-blue)}
  .chart .chart-heading{font-family:"Roboto Slab",serif;font-weight:700}

  /* photos */
  .photo{position:absolute;top:396px;height:221px}
  .photo--scaled{left:33px;width:298px;background:linear-gradient(160deg,#a09a8c 0%,#7d7568 45%,#5e5a52 100%)}
  .photo--clean{left:340px;width:187px;background:linear-gradient(200deg,#8b8a80 0%,#b3ad91 40%,#6f6b5a 100%)}
  .caption{position:absolute;top:620px;font-weight:300;font-size:10.6px;line-height:12.4px;padding-left:9px;color:var(--paper)}
  .caption::before{content:"›";position:absolute;left:0;top:-1px;font-weight:600}
  .caption--scaled{left:32px;width:296px}
  .caption--clean{left:339px;width:190px}

  /* footer */
  .footer{position:absolute;left:0;top:664px;width:560px;height:60px}
  .contact{position:absolute;font-weight:300;font-size:10.8px;color:var(--ink);padding-left:9px}
  .contact::before{content:"›";position:absolute;left:0;top:-1px;font-weight:600}
  .brand--footer{left:428px;top:22px;gap:7px}
  .brand--footer .brand__mark{width:26px;height:26px}
  .brand--footer .brand__name{font-size:9px}
</style>
</head>
<body>

<article class="page page--front">
  <header class="front-header">
    <svg width="560" height="172" viewBox="0 0 560 172" aria-hidden="true" style="position:absolute;left:0;top:0">
      <polygon points="0,85 321,85 357,172 0,172" fill="var(--band-grey)"/>
      <polygon points="343,0 350,0 328,85 364,172 357,172 321,85" fill="var(--brand-blue)"/>
    </svg>
    <div role="img" aria-label="Photo of industrial refinery towers and pipework under a hazy sky"
         style="position:absolute;left:0;top:0;width:560px;height:172px;clip-path:polygon(350px 0,560px 0,560px 172px,364px 172px,328px 85px);background:linear-gradient(180deg,#9ea3a2 0%,#7f8b89 45%,#4f6463 75%,#3c4a40 100%)"></div>
    <div class="brand brand--header">
      <span class="brand__mark"></span>
      <span class="brand__name">Ridgeline<br>Well Solutions</span>
    </div>
    <h1 class="service-title caps">Wire Burst System<br>for <span class="dark">Well Stimulation</span><br>and <span class="dark">Scale</span> <span class="blue">Removal</span><br>Services</h1>
  </header>

  <section class="panel overview">
    <h2 class="caps">Overview:</h2>
    <p class="lead">The origin of this service started in the DJ Basin when we discovered a need to increase production on older producing Plunger Lift wells. We found that after multiple rig workovers, the issue was not in the wellbore itself, but that the Perf or Slotted Sub had become either scaled or sanded off, choking the well down to very little or no flow. Realizing the issue was fixable without doing an expensive traditional Workover, we purchased a device that allows us to perform basic ballistic procedures safely off our Slickline units. There are no other standard mechanical or hydraulic slickline perforating tools that can accomplish this service. A typical job would look something like this.</p>
    <ul class="bullets">
      <li>MIRU Slickline, RIH and pull plunger noting tight spots</li>
      <li>RIH and pull BSSV – note depth of nipple so we can correlate to tubing tally and wellbore diagram</li>
      <li>RIH with “dummy run” (Keller Jars, Weight Bars, Blind Box and Temperature Probe) drift through Profile Nipples to determine Perf Sub depth, establish bottom hole temperature and locate fluid level</li>
      <li>Once depths, fluid level and temperature have been confirmed and we know we are deep enough to get into the Perf Sub, RIHW Wire Burst System® and either perforate new holes using an RTG (Retrievable Tubing Gun) or remove scale utilizing our Scale Pulse®.</li>
      <li>Free flow well to determine if new or more communication has been established.</li>
      <li>RIHW broach to production nipple. Reset production tools and turn well back to the client</li>
    </ul>
  </section>

  <svg class="chart chart--trend" viewBox="0 0 560 241" role="img" aria-label="Line chart of daily production in barrels per day from 5/3 to 5/30; production jumps from under 30 to about 60 after the Scale Pulse on 5/18">
    <text class="chart-title" x="280" y="23" text-anchor="middle" font-size="10.5" letter-spacing="1.5">Scale Pulse: Case Well #001 - Production BPD</text>
    <g stroke="var(--grid)" stroke-width="0.6">
      <line x1="57" y1="42" x2="545" y2="42"/><line x1="57" y1="57.75" x2="545" y2="57.75"/>
      <line x1="57" y1="73.5" x2="545" y2="73.5"/><line x1="57" y1="89.25" x2="545" y2="89.25"/>
      <line x1="57" y1="105" x2="545" y2="105"/><line x1="57" y1="120.75" x2="545" y2="120.75"/>
      <line x1="57" y1="136.5" x2="545" y2="136.5"/><line x1="57" y1="152.25" x2="545" y2="152.25"/>
    </g>
    <line x1="57" y1="168" x2="545" y2="168" stroke="#555" stroke-width="0.8"/>
    <g font-size="8.5" font-weight="700" text-anchor="end" fill="#222">
      <text x="37" y="45">80</text><text x="37" y="60.7">70</text><text x="37" y="76.5">60</text>
      <text x="37" y="92.2">50</text><text x="37" y="108">40</text><text x="37" y="123.7">30</text>
      <text x="37" y="139.5">20</text><text x="37" y="155.2">10</text><text x="37" y="171">0</text>
    </g>
    <polyline fill="none" stroke="var(--line)" stroke-width="2"
      points="61,158.6 78.7,166.4 96.5,158.6 114.2,146 132,160.1 149.7,134.9 167.4,139.7 185.2,152.3 202.9,123.9 220.7,128.6 238.4,150.7 256.1,142.8 273.9,152.3 291.6,146 309.4,146 327.1,127.1 344.8,62.5 362.6,71.9 380.3,75.1 398.1,92.4 415.8,76.7 433.5,76.7 451.3,78.2 469,79.8 486.8,86.1 504.5,75.1 522.2,78.2 540,86.1"/>
    <g fill="var(--brand-navy)">
      <circle cx="61" cy="158.6" r="2.8"/><circle cx="78.7" cy="166.4" r="2.8"/><circle cx="96.5" cy="158.6" r="2.8"/>
      <circle cx="114.2" cy="146" r="2.8"/><circle cx="132" cy="160.1" r="2.8"/><circle cx="149.7" cy="134.9" r="2.8"/>
      <circle cx="167.4" cy="139.7" r="2.8"/><circle cx="185.2" cy="152.3" r="2.8"/><circle cx="202.9" cy="123.9" r="2.8"/>
      <circle cx="220.7" cy="128.6" r="2.8"/><circle cx="238.4" cy="150.7" r="2.8"/><circle cx="256.1" cy="142.8" r="2.8"/>
      <circle cx="273.9" cy="152.3" r="2.8"/><circle cx="291.6" cy="146" r="2.8"/><circle cx="309.4" cy="146" r="2.8"/>
      <circle cx="327.1" cy="127.1" r="2.8"/><circle cx="344.8" cy="62.5" r="2.8"/><circle cx="362.6" cy="71.9" r="2.8"/>
      <circle cx="380.3" cy="75.1" r="2.8"/><circle cx="398.1" cy="92.4" r="2.8"/><circle cx="415.8" cy="76.7" r="2.8"/>
      <circle cx="433.5" cy="76.7" r="2.8"/><circle cx="451.3" cy="78.2" r="2.8"/><circle cx="469" cy="79.8" r="2.8"/>
      <circle cx="486.8" cy="86.1" r="2.8"/><circle cx="504.5" cy="75.1" r="2.8"/><circle cx="522.2" cy="78.2" r="2.8"/>
      <circle cx="540" cy="86.1" r="2.8"/>
    </g>
    <g font-size="8" fill="#222" text-anchor="end">
      <text transform="translate(64,173) rotate(-90)">5/3/21</text><text transform="translate(81.7,173) rotate(-90)">5/4/21</text>
      <text transform="translate(99.5,173) rotate(-90)">5/5/21</text><text transform="translate(117.2,173) rotate(-90)">5/6/21</text>
      <text transform="translate(135,173) rotate(-90)">5/7/21</text><text transform="translate(152.7,173) rotate(-90)">5/8/21</text>
      <text transform="translate(170.4,173) rotate(-90)">5/9/21</text><text transform="translate(188.2,173) rotate(-90)">5/10/21</text>
      <text transform="translate(205.9,173) rotate(-90)">5/11/21</text><text transform="translate(223.7,173) rotate(-90)">5/12/21</text>
      <text transform="translate(241.4,173) rotate(-90)">5/13/21</text><text transform="translate(259.1,173) rotate(-90)">5/14/21</text>
      <text transform="translate(276.9,173) rotate(-90)">5/15/21</text><text transform="translate(294.6,173) rotate(-90)">5/16/21</text>
      <text transform="translate(312.4,173) rotate(-90)">5/17/21</text><text transform="translate(330.1,173) rotate(-90)">5/18/21</text>
      <text transform="translate(347.8,173) rotate(-90)">5/19/21</text><text transform="translate(365.6,173) rotate(-90)">5/20/21</text>
      <text transform="translate(383.3,173) rotate(-90)">5/21/21</text><text transform="translate(401.1,173) rotate(-90)">5/22/21</text>
      <text transform="translate(418.8,173) rotate(-90)">5/23/21</text><text transform="translate(436.5,173) rotate(-90)">5/24/21</text>
      <text transform="translate(454.3,173) rotate(-90)">5/25/21</text><text transform="translate(472,173) rotate(-90)">5/26/21</text>
      <text transform="translate(489.8,173) rotate(-90)">5/27/21</text><text transform="translate(507.5,173) rotate(-90)">5/28/21</text>
      <text transform="translate(525.2,173) rotate(-90)">5/29/21</text><text transform="translate(543,173) rotate(-90)">5/30/21</text>
    </g>
    <text class="chart-title" x="280" y="229" text-anchor="middle" font-size="10.5" letter-spacing="1.5" style="fill:var(--ink)">Date - Scale Pulse Performed 5/18/2022</text>
  </svg>
</article>

<article class="page page--back">
  <svg class="chart chart--compare" viewBox="0 0 560 199" role="img" aria-label="Line chart comparing average daily production before and after the Scale Pulse service: about 13 BPD before and about 57 BPD after">
    <text class="chart-heading" x="280" y="19" text-anchor="middle" font-size="11" fill="var(--brand-blue)">Average Daily Production Before / After Scale Pulse Service - Case Well #001</text>
    <text class="chart-heading" x="280" y="34" text-anchor="middle" font-size="10.5" fill="var(--ink)">427% increase in Production</text>
    <g stroke="var(--grid)" stroke-width="0.6">
      <line x1="20" y1="50" x2="508" y2="50"/><line x1="20" y1="68.1" x2="508" y2="68.1"/>
      <line x1="20" y1="86.3" x2="508" y2="86.3"/><line x1="20" y1="104.4" x2="508" y2="104.4"/>
      <line x1="20" y1="122.6" x2="508" y2="122.6"/><line x1="20" y1="140.7" x2="508" y2="140.7"/>
      <line x1="20" y1="158.9" x2="508" y2="158.9"/><line x1="20" y1="177" x2="508" y2="177"/>
    </g>
    <g font-size="7" fill="#222" text-anchor="end">
      <text x="531" y="52.5">70.0</text><text x="531" y="70.6">60.0</text><text x="531" y="88.8">50.0</text>
      <text x="531" y="106.9">40.0</text><text x="531" y="125.1">30.0</text><text x="531" y="143.2">20.0</text>
      <text x="531" y="161.4">10.0</text><text x="531" y="179.5">0.0</text>
    </g>
    <text transform="translate(546,101) rotate(-90)" font-size="8" font-weight="700" text-anchor="middle" fill="var(--brand-blue)" style="font-family:'Raleway',sans-serif">BPD</text>
    <line x1="141" y1="153.4" x2="385" y2="73.6" stroke="var(--line)" stroke-width="2"/>
    <circle cx="141" cy="153.4" r="3" fill="var(--brand-navy)"/>
    <circle cx="385" cy="73.6" r="3" fill="var(--brand-navy)"/>
    <g font-size="7.3" fill="#222" text-anchor="middle">
      <text x="141" y="191">Average Daily Production - Before Scale Pulse</text>
      <text x="385" y="191">Average Daily Production - After Scale Pulse</text>
    </g>
  </svg>

  <section class="panel summary">
    <h2 class="caps">Summary:</h2>
    <p class="lead">This service can be done in a few hours if no unexpected well conditions are encountered. The main benefits are:</p>
    <ul class="bullets">
      <li>For a small investment, we can tell you whether or not the well needs to be worked over. If we perform this service and nothing changes, you know you have wellbore issues – NOT production tubing issues.</li>
      <li>This service is “greener” than a traditional workover, producing far less emissions. There is no need to kill the well or to flare any gas.</li>
      <li>When the service is successful, the data has shown an increase of 100%–600% in production! For example, we have stimulated wells that were making 2–3 BBL/day before we performed this service, and they are now producing 50–70 BBL/day!</li>
      <li>This service is cost-effective enough that, in most cases, the “free” increased production will pay for this service within 24–48 hours of running the well.</li>
    </ul>
  </section>

  <div class="photo photo--scaled" role="img" aria-label="Photo of a scaled-off perforated sub, painted yellow, lying on a metal grate in a shop"></div>
  <div class="photo photo--clean" role="img" aria-label="Close-up photo of the yellow perforated sub after the Scale Pulse with all holes open"></div>
  <p class="caption caption--scaled">Images 1–2: Perforated Sub recovered from a Workover rig that was completely scaled off. I painted it yellow before the test to see how much scale came off when it was stimulated using our Scale Pulse.</p>
  <p class="caption caption--clean">Perforated Sub after utilizing Scale Pulse. ALL scale removed from the sub, opening the original 56 holes.</p>

  <footer class="footer">
    <svg width="560" height="60" viewBox="0 0 560 60" aria-hidden="true" style="position:absolute;left:0;top:0">
      <rect x="0" y="14" width="560" height="46" fill="var(--band-grey)"/>
      <polygon points="418,0 560,0 560,60 418,60 397,30" fill="var(--brand-blue)"/>
      <polygon points="424,0 560,0 560,60 424,60 404,30" fill="var(--paper)"/>
    </svg>
    <span class="contact" style="left:32px;top:23px">2200 Prairie Ave Fort Morgan, CO 80701</span>
    <span class="contact" style="left:246px;top:23px">m.hale@ridgelinews.com</span>
    <span class="contact" style="left:32px;top:39px">970-555-0148</span>
    <div class="brand brand--footer">
      <span class="brand__mark"></span>
      <span class="brand__name">Ridgeline<br>Well Solutions</span>
    </div>
  </footer>
</article>

</body>
</html>
```